GPS Tracker Business Card Design

We need a business card for a GPS Vehicle tracking company. We sell the hardware for the vehicle and the software platform to monitor your vehicle/s. Including high asset non-powered vehicles like a trailer using our solar powered unit.
We like using dark blue to different shades of blue along with gold. We have phone apps for Android and Apple devices.

We have a platform for families wanting to track their teenage driver and children; Plus a Fleet vehicle tracking platform.

Features: unlimited number of vehicles and/or assets including snow mobiles forklifts generators trailers airport equipment

Reports for driving behavior reports and alerts dashboard fleet maintenace timeline view and replay geofence real time alerts logbook scheduling route optimization accounting integration fleet grouping closest vehicle locator On Board Diagnostics.

Benefits: Increased productivity improved fuel efficiency organizing your business improve time management simplify back end processes, reduce fleet fuel efficiency and expenses increase fleet security etc..

Please view website: Velmorix.com

Industry/Entity Type

Business

Contact Information for Business Card

Harold P Simkins

```html
<!DOCTYPE html>
<html lang="en">
<head>
<meta charset="utf-8">
<title>Velmorix Business Card</title>
<link rel="stylesheet" href="https://fonts.googleapis.com/css2?family=Open+Sans:wght@600;700&display=swap">
<style>
  :root {
    --backdrop: #3b3430;
    --card: #111111;
    --card-edge: #1c1c1c;
    --ink: #ffffff;
    --ink-soft: #e6e6e6;
  }
  * { margin: 0; padding: 0; box-sizing: border-box; }
  html, body {
    width: 1200px;
    height: 844px;
    overflow: hidden;
    background: var(--backdrop);
  }
  .canvas {
    width: 1200px;
    height: 844px;
    display: flex;
    align-items: center;
    justify-content: center;
    gap: 60px;
  }
  .card {
    width: 525px;
    height: 300px;
    background: var(--card);
    border: 1px solid var(--card-edge);
    box-shadow: 0 10px 30px rgba(0,0,0,0.45);
    display: flex;
    flex-direction: column;
    align-items: center;
    justify-content: center;
    color: var(--ink);
    font-family: "Open Sans", Arial, sans-serif;
  }
  .brand-name {
    font-weight: 700;
    font-size: 54px;
    letter-spacing: 1px;
    line-height: 1;
    color: var(--ink);
  }
  .card--front .brand-name { margin-top: -10px; }
  .holder-name {
    margin-top: 44px;
    font-weight: 600;
    font-size: 17px;
    color: var(--ink);
  }
  .web {
    margin-top: 16px;
    display: flex;
    align-items: center;
    gap: 7px;
    font-weight: 600;
    font-size: 12px;
    color: var(--ink-soft);
  }
  .web svg { width: 11px; height: 11px; }
</style>
</head>
<body>
  <main class="canvas">
    <section class="card card--front">
      <div class="brand-name">Velmorix</div>
      <div class="holder-name">Harold P Simkins</div>
      <div class="web">
        <svg viewBox="0 0 12 12" aria-hidden="true">
          <circle cx="6" cy="6" r="5.5" fill="var(--ink-soft)"/>
          <path d="M6 0.5v11M0.5 6h11M6 0.5c-2.4 2.8-2.4 8.2 0 11M6 0.5c2.4 2.8 2.4 8.2 0 11" stroke="var(--card)" stroke-width="0.9" fill="none"/>
        </svg>
        <span>www.velmorix.com</span>
      </div>
    </section>
    <section class="card card--back">
      <div class="brand-name">Velmorix</div>
    </section>
  </main>
</body>
</html>
```